Suds Harbor Laundromat Wordpress Design

We need a Wordpress website design for our laundromat, Suds Harbor Atlanta, at www.sudsharboratlanta-example.com. We would like to have 6 pages: Home, About Us, Services, Locations, Reviews and Contact us. We will provide content for the text on each page. What we do: We are a full service laundromat that provides dry cleaning drop off, professional laundry services, wash dry fold and self service laundry to the local community. We would like to use the color scheme from our logo to convey a warm, safe, and bright business that caters to its diverse community.
Updates

I like the structure of this laundromat website: http://www.tumblewashhub-example.com/ Using my logo and color scheme in the above referenced website is what. Am looking for. The photos attached to the project with the female model should be used as a primary focus and supplemented by actual photos of the equipment.

Target Market(s)

Our target market is a diverse group of people from Midtown Atlanta - LGBTQ community /Locals/Regulars that have been coming to laundromat for 30 years.

Industry/Entity Type

Laundromat

Coding

Coded - Design and coding required

Number of Pages Required

5+ page

Font styles to use
Sans Serif

Colors
0054AA
0677BA
7BADD7
CADEEF
E8F1F8

Requirements
Must have
• Feature this video on the main page: https://video.example.com/Qx7mBr2Lp0Z

```html
<!DOCTYPE html>
<html lang="en">
<head>
<meta charset="utf-8">
<title>Suds Harbor Laundromat</title>
<link href="https://fonts.googleapis.com/css2?family=Lobster&family=Rubik:ital,wght@0,300;0,400;0,500;1,300&display=swap" rel="stylesheet">
<style>
:root{
  --navy:#00306a;
  --blue:#0054aa;
  --mid:#0677ba;
  --sky:#7badd7;
  --pale:#cadeef;
  --mist:#e8f1f8;
  --grey-bg:#f2f4f6;
  --foot-bg:#dcf8fb;
  --text:#5c6470;
  --white:#fff;
  --steel:#8d9699;
  --steel-dark:#3e4649;
  --wall:#b9d8d3;
  --dress:#2f6fb8;
  --copper:#b8643a;
}
*{box-sizing:border-box;margin:0;padding:0}
html,body{width:1200px;height:3322px;overflow:hidden}
body{position:relative;font-family:"Rubik",sans-serif;color:var(--text);background:var(--grey-bg)}
.abs{position:absolute}
.script{font-family:"Lobster",cursive;color:var(--blue);font-weight:400}
/* header */
.site-header{left:0;top:0;width:1200px;height:93px;background:var(--white)}
.brand{left:88px;top:26px;display:flex;align-items:center;gap:10px}
.brand-dot{width:30px;height:30px;border-radius:50%;background:var(--mid)}
.brand-name{font-size:20px;font-weight:500;color:var(--blue);line-height:1.05;width:170px}
.nav{left:508px;top:40px;display:flex;gap:21px;font-size:12px;font-weight:500;color:#1d2330}
.nav .active{color:var(--mid)}
.phone{left:856px;top:37px;font-size:15px;font-style:italic;font-weight:500;color:var(--blue);display:flex;gap:8px;align-items:center}
.btn{display:flex;align-items:center;justify-content:center;border:1.5px solid var(--blue);font-size:12px;font-weight:500;color:var(--blue);background:var(--white)}
.contact-btn{left:1000px;top:28px;width:112px;height:36px;border-color:var(--mid);color:var(--mid)}
/* hero */
.hero{left:0;top:93px;width:1200px;height:667px;overflow:hidden;
  background:
    radial-gradient(ellipse 90px 260px at 600px 380px, rgba(47,111,184,.85), rgba(47,111,184,0) 100%),
    radial-gradient(ellipse 260px 120px at 420px 120px, rgba(214,170,120,.55), rgba(214,170,120,0) 100%),
    radial-gradient(ellipse 520px 260px at 600px 120px, #a9cbc6 0%, rgba(169,203,198,0) 100%),
    linear-gradient(90deg, #4b5558 0%, #9aa3a5 22%, #7f8a8c 40%, #7f8a8c 60%, #9aa3a5 78%, #4b5558 100%)}
.hero-shade{left:0;top:0;width:1200px;height:667px;background:linear-gradient(180deg,rgba(20,30,35,.15),rgba(20,30,35,.35))}
.hero-title{left:0;width:1200px;text-align:center;color:var(--white);font-size:38px;top:300px}
.hero-sub{left:340px;top:350px;width:500px;text-align:center;color:var(--white);font-size:22px;font-weight:300;line-height:27px}
/* what we do */
.section-title{width:1200px;left:0;text-align:center;font-size:40px}
.service{width:260px;text-align:center}
.service .photo{width:200px;height:200px;margin:0 auto;border-radius:50%;border:2px solid var(--sky);padding:4px}
.service .photo div{width:100%;height:100%;border-radius:50%}
.photo-a{background:radial-gradient(circle at 72% 40%, var(--copper) 0%, rgba(184,100,58,0) 34%),radial-gradient(circle at 62% 90%, var(--dress) 0%, rgba(47,111,184,0) 40%),radial-gradient(circle at 25% 55%, #3b6f9c 0%, rgba(59,111,156,0) 30%),linear-gradient(90deg,#c9cfd1,#e6e9ea 50%,#9aa1a3)}
.photo-b{background:radial-gradient(circle at 50% 65%, var(--dress) 0%, rgba(47,111,184,0) 30%),radial-gradient(circle at 50% 88%, #d9a93a 0%, rgba(217,169,58,0) 20%),linear-gradient(180deg,#d8dbdc 0%,#bfc4c6 45%,#9ea4a6 70%,#e2e4e5 100%)}
.photo-c{background:radial-gradient(circle at 55% 70%, var(--dress) 0%, rgba(47,111,184,0) 26%),radial-gradient(circle at 30% 32%, #e2b84a 0%, rgba(226,184,74,0) 14%),linear-gradient(180deg,#a9d3cd 0%,#b9dcd6 48%,#8f9799 70%,#d7dbdc 100%)}
.service h3{margin-top:20px;font-size:15px;font-weight:500;color:var(--blue)}
.service p{margin:16px auto 0;width:246px;font-size:9.5px;line-height:15px;color:#8a9099}
.service .btn{margin:22px auto 0;width:112px;height:38px}
/* about */
.about{left:0;top:1232px;width:1200px;height:650px;background:var(--navy)}
.about h2{left:88px;top:86px;font-size:36px;line-height:52px;color:var(--white)}
.about .lead{left:88px;top:197px;width:630px;font-size:10px;line-height:15px;color:var(--white)}
.ticks{top:264px;list-style:none;font-size:10.5px;font-weight:500;color:var(--white);line-height:19px}
.ticks li{display:flex;gap:10px;align-items:center}
.about .btn{left:88px;top:358px;width:112px;height:38px;background:transparent;border-color:var(--white);color:var(--white)}
.video-frame{left:774px;top:62px;width:338px;height:338px;border:1.5px solid var(--mid)}
.video{left:750px;top:86px;width:338px;height:338px;
  background:
    radial-gradient(circle at 60% 72%, #eef0f1 0%, rgba(238,240,241,0) 32%),
    radial-gradient(circle at 62% 30%, #d9c9b2 0%, rgba(217,201,178,0) 22%),
    radial-gradient(circle at 80% 25%, #c98c4a 0%, rgba(201,140,74,0) 18%),
    linear-gradient(160deg,#8fb0a8 0%,#6f8f8c 40%,#5b6664 100%)}
/* reviews */
.review{width:250px;height:275px;background:var(--white);box-shadow:0 3px 12px rgba(0,40,90,.08);padding:26px 18px}
.review .quote{font-size:30px;color:var(--mid);font-weight:300;line-height:24px;letter-spacing:-2px}
.review p{margin-top:14px;font-size:9.5px;font-style:italic;font-weight:300;line-height:18.6px;color:#8a9099}
.review h4{margin-top:14px;font-size:11px;font-weight:500;color:var(--blue)}
.review span{font-size:10px;color:var(--mid)}
/* gallery */
.gallery-bg{left:0;top:2309px;width:1200px;height:720px;background:#f7f8f9}
.shot-a{background:radial-gradient(ellipse 180px 80px at 120px 30px,#4f7a3e 0%,rgba(79,122,62,0) 100%),radial-gradient(circle at 270px 250px,#5a6064 0%,rgba(90,96,100,0) 22%),linear-gradient(180deg,#9fc4c9 0%,#b8bfc2 28%,#9aa3a6 60%,#e8e5dc 100%)}
.shot-b{background:radial-gradient(circle at 60px 90px,#4d5a62 0%,rgba(77,90,98,0) 24%),linear-gradient(180deg,#c9d5d6 0%,#a9b2b4 30%,#cfd4d5 75%,#9aa1a3 100%)}
.shot-c{background:radial-gradient(circle at 50px 30px,#d9b24a 0%,rgba(217,178,74,0) 14%),linear-gradient(180deg,#a9d3cd 0%,#b7d8d3 40%,#9aa2a5 70%,#dfe2e3 100%)}
.shot-d{background:radial-gradient(ellipse 90px 30px at 40px 20px,#5f8a50 0%,rgba(95,138,80,0) 100%),linear-gradient(180deg,#c3d8da 0%,#b2b8ba 45%,#8f9799 70%,#cfd2d3 100%)}
.arrow{width:38px;height:38px;border-radius:50%;border:1.5px solid var(--mid);display:flex;align-items:center;justify-content:center}
/* footer */
.footer{left:0;top:3019px;width:1200px;height:303px;background:var(--foot-bg)}
.footer h5{font-family:"Lobster",cursive;font-weight:400;font-size:14px;color:var(--navy)}
.footer .col{top:54px;font-size:10px;color:#3b4250;line-height:18.6px}
.contact-row{display:flex;gap:10px;align-items:flex-start}
.contact-row svg{flex:none;margin-top:3px}
.newsletter-input{width:182px;height:24px;background:#5b6f86;color:var(--white);font-size:9px;padding:7px 12px;margin-top:8px}
.send{width:100px;height:26px;margin-top:10px;border:1.5px solid var(--mid);font-size:11px;color:var(--mid);display:flex;align-items:center;justify-content:center;background:var(--white)}
.rule{left:200px;top:3256px;width:800px;height:1px;background:#b9dbe4}
.copy{left:200px;top:3278px;font-size:9px;color:#7a8190}
.copy b{color:var(--blue);font-weight:500}
.social{top:3271px;width:24px;height:24px;border-radius:50%;background:var(--blue)}
</style>
</head>
<body>

<header class="site-header abs">
  <div class="brand abs"><span class="brand-dot"></span><span class="brand-name">Suds Harbor Laundromat</span></div>
  <nav class="nav abs"><span class="active">Home</span><span>About Us</span><span>Services</span><span>Locations</span><span>Reviews</span></nav>
  <div class="phone abs">
    <svg width="14" height="14" viewBox="0 0 24 24" fill="none" stroke="#0054aa" stroke-width="2"><path d="M22 16.9v3a2 2 0 0 1-2.2 2 19.8 19.8 0 0 1-8.6-3.1 19.5 19.5 0 0 1-6-6A19.8 19.8 0 0 1 2.1 4.2 2 2 0 0 1 4.1 2h3a2 2 0 0 1 2 1.7c.1 1 .4 1.9.7 2.8a2 2 0 0 1-.5 2.1L8 9.9a16 16 0 0 0 6 6l1.3-1.3a2 2 0 0 1 2.1-.4c.9.3 1.8.6 2.8.7a2 2 0 0 1 1.7 2z"/></svg>
    404-555-0182
  </div>
  <a class="btn contact-btn abs">Contact Us</a>
</header>

<section class="hero abs" role="img" aria-label="Photo of a woman in a blue dress walking between rows of washers and dryers under the laundromat wall sign">
  <div class="hero-shade abs"></div>
  <h1 class="hero-title abs script">Laundromat for 30 Years</h1>
  <p class="hero-sub abs">Coin Laundry, Dry Cleaning, and Professional Laundry</p>
  <svg class="abs" style="left:590px;top:460px" width="20" height="26" viewBox="0 0 20 26" fill="none" stroke="#fff" stroke-width="1.6"><path d="M10 2v21M3 16l7 7 7-7"/></svg>
  <svg class="abs" style="left:0;top:0" width="1200" height="667" viewBox="0 0 1200 667">
    <path d="M0 590 C200 440 380 520 560 560 C760 600 980 560 1200 420 L1200 667 L0 667Z" fill="#1f5fa6"/>
    <path d="M0 640 C220 470 400 560 600 600 C800 640 1000 590 1200 440 L1200 667 L0 667Z" fill="#fff"/>
    <path d="M0 650 C220 490 400 580 600 620 C800 660 1000 610 1200 460 L1200 667 L0 667Z" fill="#f2f4f6"/>
  </svg>
</section>

<h2 class="section-title abs script" style="top:734px">What We Do</h2>
<div class="service abs" style="left:195px;top:803px">
  <div class="photo"><div class="photo-a" role="img" aria-label="Photo of a woman looking into a front-load washer"></div></div>
  <h3>Dry Cleaning Drop Off</h3>
  <p>It is a long established fact that a reader will be distracted by the readable content of a page when looking at its layout. The point of using Lorem Ipsum is that it has a more-or-less normal ...</p>
  <a class="btn">Read More</a>
</div>
<div class="service abs" style="left:470px;top:803px">
  <div class="photo"><div class="photo-b" role="img" aria-label="Photo of a woman seated in front of a row of washers"></div></div>
  <h3>Professional Laundry Services</h3>
  <p>It is a long established fact that a reader will be distracted by the readable content of a page when looking at its layout. The point of using Lorem Ipsum is that it has a more-or-less normal ...</p>
  <a class="btn">Read More</a>
</div>
<div class="service abs" style="left:745px;top:803px">
  <div class="photo"><div class="photo-c" role="img" aria-label="Photo of a woman standing below the laundromat wall sign"></div></div>
  <h3>Wash Dry Fold</h3>
  <p>It is a long established fact that a reader will be distracted by the readable content of a page when looking at its layout. The point of using Lorem Ipsum is that it has a more-or-less normal ...</p>
  <a class="btn">Read More</a>
</div>

<section class="about abs">
  <h2 class="abs script" style="color:#fff">Coin Laundry, Dry Cleaning, &amp;<br>Professional Laundry</h2>
  <p class="lead abs">There are many variations of passages of Lorem Ipsum available, but the majority have suffered alteration in some form, by injected humour, or randomised words which don't look even slightly believable. If you are going to use a passage of Lorem Ipsum, you need to be sure there isn't anything embarrassing hidden in the middle of text.</p>
  <ul class="ticks abs" style="left:88px">
    <li><svg width="12" height="10" viewBox="0 0 12 10" fill="none" stroke="#fff" stroke-width="1.4"><path d="M1 5l3 3 7-7"/></svg>In Business over 45 years</li>
    <li><svg width="12" height="10" viewBox="0 0 12 10" fill="none" stroke="#fff" stroke-width="1.4"><path d="M1 5l3 3 7-7"/></svg>Voted "BEST COIN LAUNDRY" - Multiple years</li>
    <li><svg width="12" height="10" viewBox="0 0 12 10" fill="none" stroke="#fff" stroke-width="1.4"><path d="M1 5l3 3 7-7"/></svg>The best Wash-Dry-Fold in town</li>
    <li><svg width="12" height="10" viewBox="0 0 12 10" fill="none" stroke="#fff" stroke-width="1.4"><path d="M1 5l3 3 7-7"/></svg>Over 50 well maintained machines</li>
  </ul>
  <ul class="ticks abs" style="left:381px">
    <li><svg width="12" height="10" viewBox="0 0 12 10" fill="none" stroke="#fff" stroke-width="1.4"><path d="M1 5l3 3 7-7"/></svg>In Business over 45 years</li>
    <li><svg width="12" height="10" viewBox="0 0 12 10" fill="none" stroke="#fff" stroke-width="1.4"><path d="M1 5l3 3 7-7"/></svg>One of Atlanta's First, Finest, &amp; Friendliest Coin Laundries</li>
    <li><svg width="12" height="10" viewBox="0 0 12 10" fill="none" stroke="#fff" stroke-width="1.4"><path d="M1 5l3 3 7-7"/></svg>Cool - Comfortable - Clean</li>
    <li><svg width="12" height="10" viewBox="0 0 12 10" fill="none" stroke="#fff" stroke-width="1.4"><path d="M1 5l3 3 7-7"/></svg>Commercial Accounts</li>
  </ul>
  <a class="btn abs">About Us</a>
  <div class="video-frame abs"></div>
  <div class="video abs" role="img" aria-label="Video still: customer carrying a laundry basket inside the laundromat">
    <svg class="abs" style="left:151px;top:151px" width="36" height="36" viewBox="0 0 36 36" fill="none" stroke="#fff" stroke-width="2"><circle cx="18" cy="18" r="16"/><path d="M14 11l11 7-11 7z"/></svg>
  </div>
  <svg class="abs" style="left:0;top:430px" width="1200" height="220" viewBox="0 0 1200 220">
    <path d="M0 140 C120 70 220 30 340 40 C520 60 640 170 820 160 C960 150 1080 110 1200 40 L1200 220 L0 220Z" fill="#1f5fa6"/>
    <path d="M0 185 C130 90 230 55 350 62 C530 80 650 190 830 182 C970 175 1090 130 1200 60 L1200 220 L0 220Z" fill="#fff"/>
    <path d="M0 200 C130 105 230 70 350 77 C530 95 650 205 830 197 C970 190 1090 145 1200 75 L1200 220 L0 220Z" fill="#f2f4f6"/>
  </svg>
</section>

<h2 class="section-title abs script" style="top:1904px">Client Reviews</h2>
<div class="review abs" style="left:200px;top:1971px"><div class="quote">66</div><p>"There are many variations of passages of Lorem Ipsum available, but the majority have suffered alteration in some form, by injected humour, or randomised words which don't look even slightly believable. If you are going to use a passage of Lorem Ipsum, you need to be sure there isn't anything embarrassing"</p><h4>Standard Chunk</h4><span>popular belief</span></div>
<div class="review abs" style="left:475px;top:1971px"><div class="quote">66</div><p>"There are many variations of passages of Lorem Ipsum available, but the majority have suffered alteration in some form, by injected humour, or randomised words which don't look even slightly believable. If you are going to use a passage of Lorem Ipsum, you need to be sure there isn't anything embarrassing"</p><h4>Standard Chunk</h4><span>popular belief</span></div>
<div class="review abs" style="left:750px;top:1971px"><div class="quote">66</div><p>"There are many variations of passages of Lorem Ipsum available, but the majority have suffered alteration in some form, by injected humour, or randomised words which don't look even slightly believable. If you are going to use a passage of Lorem Ipsum, you need to be sure there isn't anything embarrassing"</p><h4>Standard Chunk</h4><span>popular belief</span></div>

<div class="gallery-bg abs"></div>
<h2 class="section-title abs script" style="top:2362px">Equipment Gallery</h2>
<div class="shot-a abs" style="left:200px;top:2429px;width:387px;height:337px" role="img" aria-label="Photo of stainless steel front-load washers with plants behind"></div>
<div class="shot-b abs" style="left:613px;top:2429px;width:387px;height:156px" role="img" aria-label="Photo of a long row of numbered dryers"></div>
<div class="shot-c abs" style="left:613px;top:2611px;width:180px;height:155px" role="img" aria-label="Photo of washers below the wall sign"></div>
<div class="shot-d abs" style="left:818px;top:2611px;width:182px;height:155px" role="img" aria-label="Photo of the laundromat aisle with machines on both sides"></div>
<div class="arrow abs" style="left:124px;top:2578px"><svg width="14" height="10" viewBox="0 0 14 10" fill="none" stroke="#0677ba" stroke-width="1.3"><path d="M13 5H1M5 1L1 5l4 4"/></svg></div>
<div class="arrow abs" style="left:1036px;top:2578px"><svg width="14" height="10" viewBox="0 0 14 10" fill="none" stroke="#0677ba" stroke-width="1.3"><path d="M1 5h12M9 1l4 4-4 4"/></svg></div>

<svg class="abs" style="left:0;top:2820px" width="1200" height="200" viewBox="0 0 1200 200">
  <path d="M0 120 C120 50 220 20 340 25 C520 40 640 150 820 140 C960 132 1080 95 1200 30 L1200 200 L0 200Z" fill="#1f5fa6"/>
  <path d="M0 165 C130 75 230 42 350 47 C530 62 650 172 830 164 C970 157 1090 115 1200 50 L1200 200 L0 200Z" fill="#fff"/>
  <path d="M0 180 C130 90 230 57 350 62 C530 77 650 187 830 179 C970 172 1090 130 1200 65 L1200 200 L0 200Z" fill="#dcf8fb"/>
</svg>

<footer class="footer abs">
  <div class="abs" style="left:200px;top:54px;display:flex;align-items:center;gap:10px">
    <span class="brand-dot"></span><span class="brand-name" style="width:160px">Suds Harbor Laundromat</span>
  </div>
  <div class="col abs" style="left:406px">
    <h5>Contact Us</h5>
    <div class="contact-row" style="margin-top:8px;font-size:13px;color:var(--blue)"><svg width="12" height="12" viewBox="0 0 24 24" fill="none" stroke="#0677ba" stroke-width="2"><path d="M22 16.9v3a2 2 0 0 1-2.2 2 19.8 19.8 0 0 1-8.6-3.1 19.5 19.5 0 0 1-6-6A19.8 19.8 0 0 1 2.1 4.2 2 2 0 0 1 4.1 2h3a2 2 0 0 1 2 1.7c.1 1 .4 1.9.7 2.8a2 2 0 0 1-.5 2.1L8 9.9a16 16 0 0 0 6 6l1.3-1.3a2 2 0 0 1 2.1-.4c.9.3 1.8.6 2.8.7a2 2 0 0 1 1.7 2z"/></svg>(404) 555-0182</div>
    <div class="contact-row"><svg width="12" height="12" viewBox="0 0 24 24" fill="none" stroke="#0677ba" stroke-width="2"><rect x="2" y="5" width="20" height="14"/><path d="M2 6l10 7 10-7"/></svg>hello@sudsharbor-example.com</div>
    <div class="contact-row" style="margin-top:12px"><svg width="12" height="12" viewBox="0 0 24 24" fill="none" stroke="#0677ba" stroke-width="2"><path d="M12 22s7-7 7-12a7 7 0 0 0-14 0c0 5 7 12 7 12z"/><circle cx="12" cy="10" r="2.5"/></svg><span style="line-height:15px">Harbor Point Plaza,<br>2210 Maple Grove Ave NE., # 12, Atlanta,<br>GA 30309</span></div>
  </div>
  <div class="col abs" style="left:669px">
    <h5>Quick Links</h5>
    <div style="margin-top:6px">Home<br>About Us<br>Services<br>Locations<br>Reviews<br>Contact Us</div>
  </div>
  <div class="col abs" style="left:818px">
    <h5>Sign Up Newsletter</h5>
    <p style="margin-top:6px;line-height:14px;width:190px">There are many variations of passages lorem Ipsum available</p>
    <div class="newsletter-input">Enter your email ...</div>
    <div class="send">Send</div>
  </div>
</footer>
<div class="rule abs"></div>
<p class="copy abs">© 2021 <b>Suds Harbor Atlanta</b> All Right Reserved</p>
<span class="social abs" style="left:819px"></span>
<span class="social abs" style="left:851px;background:var(--mid)"></span>
<svg class="abs" style="left:1048px;top:3268px" width="16" height="24" viewBox="0 0 16 24" fill="none" stroke="#0677ba" stroke-width="1.5"><path d="M8 23V2M1 9l7-7 7 7"/></svg>

</body>
</html>
```